KORBALT

The business want a professional looking business card. We have a scetch we will add but want the extra upgrade, and would like more suggestions for variations of our business cards.

```html
<!DOCTYPE html>
<html lang="en">
<head>
<meta charset="utf-8">
<title>KORBALT – Business Card</title>
<link rel="stylesheet" href="https://fonts.googleapis.com/css2?family=Montserrat:wght@300;400;600;700&family=Lato:wght@400&display=swap">
<style>
  :root {
    --backdrop: #9a9a9a;
    --card: #000000;
    --gold: #c9a45e;
    --gold-light: #ecc97a;
    --gold-dark: #7a5a2a;
    --gold-soft: #b8955a;
  }
  * { margin: 0; padding: 0; box-sizing: border-box; }
  html, body { width: 1200px; height: 1059px; overflow: hidden; }
  body { background: var(--backdrop); position: relative; font-family: "Montserrat", sans-serif; }

  .card {
    position: absolute;
    background: var(--card);
    border-radius: 26px;
    overflow: hidden;
  }
  .card-front { left: 256px; top: 84px; width: 688px; height: 404px; }
  .card-back  { left: 240px; top: 566px; width: 707px; height: 429px; }

  .brand { position: absolute; text-align: center; color: var(--gold); }
  .brand-dot { display: block; margin: 0 auto; border-radius: 50%; background: var(--gold); }
  .brand-name { display: block; font-family: "Montserrat", sans-serif; font-weight: 600; color: var(--gold); }

  .card-front .brand { left: 48px; width: 240px; top: 120px; }
  .card-front .brand-dot { width: 44px; height: 44px; margin-bottom: 38px; }
  .card-front .brand-name { font-size: 24px; letter-spacing: 7px; padding-left: 7px; }

  .card-back .brand { left: 0; width: 707px; top: 130px; }
  .card-back .brand-dot { width: 74px; height: 74px; margin-bottom: 62px; }
  .card-back .brand-name { font-size: 38px; letter-spacing: 11px; padding-left: 11px; }

  .divider {
    position: absolute; left: 294px; top: 88px; width: 1px; height: 182px;
    background: linear-gradient(var(--gold-dark), var(--gold-soft), var(--gold-dark));
  }

  .person { position: absolute; left: 326px; top: 82px; }
  .person-name { font-weight: 700; font-size: 26.5px; color: var(--gold); letter-spacing: 0.2px; }
  .person-role { font-weight: 300; font-size: 18.5px; color: var(--gold-soft); margin-top: 4px; }

  .contacts { position: absolute; left: 326px; top: 172px; list-style: none; }
  .contact { display: flex; align-items: center; height: 30px; margin-bottom: 2px;
    font-family: "Lato", sans-serif; font-size: 18.5px; color: var(--gold); }
  .contact svg { width: 22px; height: 22px; margin-right: 12px; fill: var(--gold); }

  .gold-band { position: absolute; left: 0; bottom: 0; width: 688px; height: 16px; }
</style>
</head>
<body>

  <section class="card card-front">
    <div class="brand">
      <span class="brand-dot"></span>
      <span class="brand-name">KORBALT</span>
    </div>

    <div class="divider"></div>

    <div class="person">
      <h1 class="person-name">Lars Olav Brekkestad</h1>
      <p class="person-role">CEO &amp; Founder</p>
    </div>

    <ul class="contacts">
      <li class="contact">
        <svg viewBox="0 0 24 24"><path d="M6.6 10.8c1.4 2.8 3.8 5.1 6.6 6.6l2.2-2.2c.3-.3.7-.4 1-.2 1.1.4 2.3.6 3.6.6.6 0 1 .4 1 1V20c0 .6-.4 1-1 1C10.6 21 3 13.4 3 4c0-.6.4-1 1-1h3.5c.6 0 1 .4 1 1 0 1.3.2 2.5.6 3.6.1.3 0 .7-.2 1L6.6 10.8z"/></svg>
        004791234567
      </li>
      <li class="contact">
        <svg viewBox="0 0 24 24"><path d="M12 2a10 10 0 1 0 0 20 10 10 0 0 0 0-20zm-1 17.9A8 8 0 0 1 4.2 10.2L9 15v1c0 1.1.9 2 2 2v1.9zm6.9-2.5c-.3-.8-1-1.4-1.9-1.4h-1v-3c0-.6-.4-1-1-1H8v-2h2c.6 0 1-.4 1-1V7h2c1.1 0 2-.9 2-2v-.4a8 8 0 0 1 2.9 12.8z"/></svg>
        www.korbalt.llc
      </li>
      <li class="contact">
        <svg viewBox="0 0 24 24"><path d="M2 5h20v14H2V5zm2 2v.5l8 5 8-5V7l-8 5-8-5z"/></svg>
        korbalt.llc@mailhub.com
      </li>
    </ul>

    <svg class="gold-band" viewBox="0 0 688 16" preserveAspectRatio="none" aria-hidden="true">
      <defs>
        <linearGradient id="bandGold" x1="0" x2="1" y1="0" y2="0">
          <stop offset="0" stop-color="#7a5a2a"/>
          <stop offset="0.45" stop-color="#e6c27a"/>
          <stop offset="0.6" stop-color="#e0bc70"/>
          <stop offset="1" stop-color="#8a6630"/>
        </linearGradient>
      </defs>
      <rect x="0" y="0" width="688" height="16" fill="url(#bandGold)"/>
      <polygon points="348,0 362,0 338,16 324,16" fill="#000"/>
    </svg>
  </section>

  <section class="card card-back">
    <div class="brand">
      <span class="brand-dot"></span>
      <span class="brand-name">KORBALT</span>
    </div>
  </section>

</body>
</html>
```